Recipe mobile app, new flow and design for uploading recipe process

I need a new recipe upload process that's simple, intuitive, and engaging.
The goal is to have a user-friendly and fast flow.
The app is a social recipe library where anyone can upload a recipe after signing up. I currently have a flow, but it's "boring," so I'd like to significantly improve this aspect of the app.
When I create a new recipe, it's immediately saved and labeled as a draft. I'll then need to specify:
- Recipe title
- Cover image (required)
- Number of people (how many people is the recipe for)
- Ingredients (name, quantity, and unit of measurement)
- Recipe explanation (broken down into steps, and I can optionally attach an image to each step)
- Upload
Every change is immediately saved, so you can edit, exit, and resume editing later.
I've attached images of the app and the current upload process.
Thank you.
Low design quality
Good morning everyone,
some of the designs received are fantastic, but please make sure to carefully read the requirement so as not to do extra work.
The requirement is to redesign the flow that a user follows when uploading a recipe to the platform.
We have uploaded the current app screens to give you an idea of what the product looks like, what the colors and style are, but we don’t need a full redesign - only the part mentioned above, while keeping the existing style and colors (we cannot rework the entire theme).
To clarify: if you look at the screens shared in the zip file attached to the project, the focus should be on the screens from 5_.png to 10_.png.
These screens can be redesigned in the most creative way you think, as long as the overall theme remains unchanged.
Thank you for your attention.

```html
<!DOCTYPE html>
<html lang="en">
<head>
<meta charset="utf-8">
<title>Recipe Upload Flow</title>
<link href="https://fonts.googleapis.com/css2?family=Poppins:wght@400;500;600;700&display=swap" rel="stylesheet">
<style>
:root{
  --bg:#24A55C;
  --bg-deep:#178C45;
  --screen:#F4F4F4;
  --card:#FFFFFF;
  --green:#22A15A;
  --orange:#FF8447;
  --ink:#1E1E1E;
  --muted:#9A9A9A;
  --line:#D6D6D6;
}
*{box-sizing:border-box;margin:0;padding:0}
html,body{width:937px;height:1200px;overflow:hidden}
body{background:var(--bg);font-family:'Poppins',sans-serif;color:var(--ink);position:relative}
.halo{position:absolute;left:107px;top:238px;width:722px;height:722px;border-radius:50%;background:var(--bg-deep)}
.phone{position:absolute;width:236px;height:522px;border-radius:22px;background:var(--screen);box-shadow:0 10px 24px rgba(0,0,0,.18);overflow:hidden}
.status{position:absolute;top:11px;left:14px;right:16px;display:flex;justify-content:space-between;align-items:center;font-size:9px}
.status svg{display:block}
.topbar{position:absolute;top:40px;left:14px;right:15px;height:16px;display:flex;align-items:center;justify-content:space-between}
.topbar .title{position:absolute;left:0;right:0;text-align:center;font-size:9.5px;font-weight:600;pointer-events:none}
.topbar .action{font-size:9.5px;font-weight:600;color:var(--green);position:relative}
.topbar .action.small{font-size:8.5px}
.home-bar{position:absolute;left:71px;bottom:21px;width:93px;height:3.5px;border-radius:2px;background:#111}
.search{position:absolute;top:64px;left:15px;width:207px;height:30px;border:1px solid var(--line);border-radius:7px;background:var(--card);display:flex;align-items:center;padding:0 10px;gap:7px;font-size:8px}
.search .value{flex:1}
.search .placeholder{flex:1;color:var(--muted)}
.dropzone{position:absolute;top:103px;left:16px;width:206px;height:142px;border:1px dashed #8F8F8F;border-radius:7px;padding:5px}
.dropzone .inner{width:100%;height:100%;background:var(--card);border-radius:5px;display:flex;flex-direction:column;align-items:center;padding-top:13px}
.dropzone .label{font-size:8px;margin-top:9px}
.btn{margin-top:10px;width:95px;height:25px;border-radius:4px;background:var(--green);color:#fff;font-size:7.5px;font-weight:600;display:flex;align-items:center;justify-content:center}
.cover-photo{width:100%;height:100%;border-radius:5px;background:linear-gradient(180deg,#8a6347 0%,#b88d64 55%,#e6e0d8 100%)}
.question{position:absolute;top:80px;left:14px;font-size:7.8px}
.stepper-field{position:absolute;top:96px;left:15px;width:207px;height:30px;border:1px solid var(--line);border-radius:7px;background:var(--card);display:flex;align-items:center;padding:0 5px 0 11px}
.stepper-field span{flex:1;color:var(--muted);font-size:7px}
.stepper-field .arrows{width:24px;height:20px;border-radius:5px;background:#F0F0F0;display:flex;align-items:center;justify-content:center}
.fab{position:absolute;right:15px;top:438px;width:28px;height:28px;border-radius:50%;background:var(--orange);display:flex;align-items:center;justify-content:center}
.ingredient{position:absolute;left:15px;width:207px;height:36px;background:var(--card);border-radius:6px;box-shadow:0 1px 3px rgba(0,0,0,.08);display:flex;align-items:center;padding-left:4px}
.ingredient .thumb{width:31px;height:30px;border-radius:4px}
.ingredient .name{width:58px;margin-left:6px;font-size:8px;font-weight:600}
.ingredient .qty{width:31px;height:30px;border-radius:5px;background:#F2F2F2;font-size:7.8px;display:flex;align-items:center;justify-content:center}
.ingredient .unit{margin-left:4px;width:68px;height:30px;border:1px solid var(--line);border-radius:5px;font-size:7.8px;display:flex;align-items:center;justify-content:space-between;padding:0 6px}
.step{position:absolute;width:92px;height:138px;background:var(--card);border-radius:6px;box-shadow:0 1px 3px rgba(0,0,0,.08)}
.step .photo{position:absolute;top:3px;left:3px;right:3px;height:85px;border-radius:4px}
.step .num{position:absolute;top:79px;left:10px;width:19px;height:19px;border-radius:50%;background:var(--green);border:2px solid #fff;color:#fff;font-size:5px;font-weight:700;display:flex;align-items:center;justify-content:center}
.step p{position:absolute;top:102px;left:11px;right:8px;font-size:5.8px;font-weight:500;line-height:1.6}
</style>
</head>
<body>
<div class="halo"></div>

<!-- Screen 1: name & cover, empty -->
<section class="phone" style="left:55px;top:53px">
  <div class="status"><span>3:43</span><svg width="40" height="8" viewBox="0 0 40 8"><path d="M1 3a6 6 0 0 1 8 0M2.5 4.5a4 4 0 0 1 5 0M5 7l1.2-1.2a1.7 1.7 0 0 0-2.4 0z" stroke="#111" stroke-width="1" fill="#111"/><path d="M15 7h1V6h-1zM17 7h1V4.5h-1zM19 7h1V3h-1zM21 7h1V1h-1z" fill="#111"/><rect x="28" y="1" width="9" height="6" rx="1" fill="none" stroke="#111"/><rect x="29.5" y="2.5" width="6" height="3" fill="#111"/><rect x="37.5" y="3" width="1" height="2" fill="#111"/></svg></div>
  <div class="topbar"><svg width="8" height="10" viewBox="0 0 8 10"><path d="M6 1L2 5l4 4" stroke="#111" stroke-width="1.4" fill="none"/></svg><span class="action">Next</span></div>
  <div class="search"><svg width="13" height="9" viewBox="0 0 13 9"><path d="M1.5 7a5 5 0 0 1 10 0z" fill="#B8B8B8"/><rect x="0" y="7.3" width="13" height="1.4" rx=".7" fill="#B8B8B8"/><circle cx="6.5" cy="1.3" r="1" fill="#B8B8B8"/></svg><span class="placeholder">Recipe name</span><svg width="8" height="8" viewBox="0 0 8 8"><circle cx="3.3" cy="3.3" r="2.5" stroke="#999" fill="none"/><path d="M5.2 5.2L7.5 7.5" stroke="#999"/></svg></div>
  <div class="dropzone"><div class="inner">
    <svg width="44" height="43" viewBox="0 0 44 43" fill="none" stroke="#A8A8A8" stroke-width="2.4" stroke-linecap="round" stroke-linejoin="round"><path d="M26 4H10a7 7 0 0 0-7 7v22a7 7 0 0 0 7 7h24a7 7 0 0 0 7-7V20"/><circle cx="15" cy="15" r="3.5"/><path d="M3 34l9-8c3-2.5 6-2 8 0l4 4c2 2 5 2 7 0l10-8"/><path d="M34 14V2M29 7l5-5 5 5"/></svg>
    <span class="label">Upload Image</span>
    <span class="btn">Browse File</span>
  </div></div>
  <div class="home-bar"></div>
</section>

<!-- Screen 2: name & cover, filled -->
<section class="phone" style="left:351px;top:53px">
  <div class="status"><span>3:43</span><svg width="40" height="8" viewBox="0 0 40 8"><path d="M1 3a6 6 0 0 1 8 0M2.5 4.5a4 4 0 0 1 5 0M5 7l1.2-1.2a1.7 1.7 0 0 0-2.4 0z" stroke="#111" stroke-width="1" fill="#111"/><path d="M15 7h1V6h-1zM17 7h1V4.5h-1zM19 7h1V3h-1zM21 7h1V1h-1z" fill="#111"/><rect x="28" y="1" width="9" height="6" rx="1" fill="none" stroke="#111"/><rect x="29.5" y="2.5" width="6" height="3" fill="#111"/><rect x="37.5" y="3" width="1" height="2" fill="#111"/></svg></div>
  <div class="topbar"><svg width="8" height="10" viewBox="0 0 8 10"><path d="M6 1L2 5l4 4" stroke="#111" stroke-width="1.4" fill="none"/></svg><span class="action">Next</span></div>
  <div class="search"><svg width="13" height="9" viewBox="0 0 13 9"><path d="M1.5 7a5 5 0 0 1 10 0z" fill="#22A15A"/><rect x="0" y="7.3" width="13" height="1.4" rx=".7" fill="#22A15A"/><circle cx="6.5" cy="1.3" r="1" fill="#22A15A"/></svg><span class="value">Tiramisu</span><svg width="8" height="8" viewBox="0 0 8 8"><circle cx="3.3" cy="3.3" r="2.5" stroke="#999" fill="none"/><path d="M5.2 5.2L7.5 7.5" stroke="#999"/></svg></div>
  <div class="dropzone"><div class="cover-photo" role="img" aria-label="Cover photo of a slice of tiramisu on a plate"></div></div>
  <div class="home-bar"></div>
</section>

<!-- Screen 3: servings -->
<section class="phone" style="left:646px;top:53px">
  <div class="status"><span>3:43</span><svg width="40" height="8" viewBox="0 0 40 8"><path d="M1 3a6 6 0 0 1 8 0M2.5 4.5a4 4 0 0 1 5 0M5 7l1.2-1.2a1.7 1.7 0 0 0-2.4 0z" stroke="#111" stroke-width="1" fill="#111"/><path d="M15 7h1V6h-1zM17 7h1V4.5h-1zM19 7h1V3h-1zM21 7h1V1h-1z" fill="#111"/><rect x="28" y="1" width="9" height="6" rx="1" fill="none" stroke="#111"/><rect x="29.5" y="2.5" width="6" height="3" fill="#111"/><rect x="37.5" y="3" width="1" height="2" fill="#111"/></svg></div>
  <div class="topbar"><svg width="8" height="10" viewBox="0 0 8 10"><path d="M6 1L2 5l4 4" stroke="#111" stroke-width="1.4" fill="none"/></svg><span class="title">Ingredients</span><span class="action">Next</span></div>
  <p class="question">For how many persons is this recipe?</p>
  <div class="stepper-field"><span>Ex : 4</span><div class="arrows"><svg width="6" height="8" viewBox="0 0 6 8"><path d="M0 3l3-3 3 3zM0 5l3 3 3-3z" fill="#555"/></svg></div></div>
  <div class="fab"><svg width="12" height="12" viewBox="0 0 12 12"><path d="M6 1v10M1 6h10" stroke="#fff" stroke-width="1.4"/></svg></div>
  <div class="home-bar"></div>
</section>

<!-- Screen 4: ingredients list -->
<section class="phone" style="left:55px;top:626px">
  <div class="status"><span>3:43</span><svg width="40" height="8" viewBox="0 0 40 8"><path d="M1 3a6 6 0 0 1 8 0M2.5 4.5a4 4 0 0 1 5 0M5 7l1.2-1.2a1.7 1.7 0 0 0-2.4 0z" stroke="#111" stroke-width="1" fill="#111"/><path d="M15 7h1V6h-1zM17 7h1V4.5h-1zM19 7h1V3h-1zM21 7h1V1h-1z" fill="#111"/><rect x="28" y="1" width="9" height="6" rx="1" fill="none" stroke="#111"/><rect x="29.5" y="2.5" width="6" height="3" fill="#111"/><rect x="37.5" y="3" width="1" height="2" fill="#111"/></svg></div>
  <div class="topbar"><svg width="8" height="10" viewBox="0 0 8 10"><path d="M6 1L2 5l4 4" stroke="#111" stroke-width="1.4" fill="none"/></svg><span class="title">Ingredients</span><span class="action">Next</span></div>
  <p class="question">For how many persons is this recipe?</p>
  <div class="stepper-field"><span>Ex : 4</span><div class="arrows"><svg width="6" height="8" viewBox="0 0 6 8"><path d="M0 3l3-3 3 3zM0 5l3 3 3-3z" fill="#555"/></svg></div></div>

  <div class="ingredient" style="top:134px"><div class="thumb" role="img" aria-label="Photo of milk" style="background:linear-gradient(135deg,#b9d9a8,#ecece6)"></div><span class="name">Milk</span><span class="qty">250.0</span><span class="unit">Milliliters<svg width="6" height="4" viewBox="0 0 6 4"><path d="M0 0h6L3 4z" fill="#333"/></svg></span></div>
  <div class="ingredient" style="top:178px"><div class="thumb" role="img" aria-label="Photo of sugar" style="background:linear-gradient(135deg,#d8d2cc,#8b6a55)"></div><span class="name">Sugar</span><span class="qty">0.0</span><span class="unit">As Needed<svg width="6" height="4" viewBox="0 0 6 4"><path d="M0 0h6L3 4z" fill="#333"/></svg></span></div>
  <div class="ingredient" style="top:222px"><div class="thumb" role="img" aria-label="Photo of chocolate" style="background:linear-gradient(135deg,#74402a,#4a2617)"></div><span class="name">Chocolate</span><span class="qty">10.0</span><span class="unit">Grams<svg width="6" height="4" viewBox="0 0 6 4"><path d="M0 0h6L3 4z" fill="#333"/></svg></span></div>
  <div class="ingredient" style="top:266px"><div class="thumb" role="img" aria-label="Photo of eggs" style="background:linear-gradient(135deg,#d9b39a,#9a6446)"></div><span class="name">Eggs</span><span class="qty">5.0</span><span class="unit">Pieces<svg width="6" height="4" viewBox="0 0 6 4"><path d="M0 0h6L3 4z" fill="#333"/></svg></span></div>
  <div class="ingredient" style="top:310px"><div class="thumb" role="img" aria-label="Photo of a glass of water" style="background:linear-gradient(135deg,#8cbf63,#cfe5c3)"></div><span class="name">Water</span><span class="qty">500.0</span><span class="unit">Milliliters<svg width="6" height="4" viewBox="0 0 6 4"><path d="M0 0h6L3 4z" fill="#333"/></svg></span></div>

  <div class="fab"><svg width="12" height="12" viewBox="0 0 12 12"><path d="M6 1v10M1 6h10" stroke="#fff" stroke-width="1.4"/></svg></div>
  <div class="home-bar"></div>
</section>

<!-- Screen 5: steps, empty -->
<section class="phone" style="left:351px;top:626px">
  <div class="status"><span>3:43</span><svg width="40" height="8" viewBox="0 0 40 8"><path d="M1 3a6 6 0 0 1 8 0M2.5 4.5a4 4 0 0 1 5 0M5 7l1.2-1.2a1.7 1.7 0 0 0-2.4 0z" stroke="#111" stroke-width="1" fill="#111"/><path d="M15 7h1V6h-1zM17 7h1V4.5h-1zM19 7h1V3h-1zM21 7h1V1h-1z" fill="#111"/><rect x="28" y="1" width="9" height="6" rx="1" fill="none" stroke="#111"/><rect x="29.5" y="2.5" width="6" height="3" fill="#111"/><rect x="37.5" y="3" width="1" height="2" fill="#111"/></svg></div>
  <div class="topbar"><svg width="8" height="10" viewBox="0 0 8 10"><path d="M6 1L2 5l4 4" stroke="#111" stroke-width="1.4" fill="none"/></svg><span class="title">Steps</span><span class="action small">Upload recipe</span></div>
  <div class="fab"><svg width="12" height="12" viewBox="0 0 12 12"><path d="M6 1v10M1 6h10" stroke="#fff" stroke-width="1.4"/></svg></div>
  <div class="home-bar"></div>
</section>

<!-- Screen 6: steps, filled -->
<section class="phone" style="left:646px;top:626px">
  <div class="status"><span>3:43</span><svg width="40" height="8" viewBox="0 0 40 8"><path d="M1 3a6 6 0 0 1 8 0M2.5 4.5a4 4 0 0 1 5 0M5 7l1.2-1.2a1.7 1.7 0 0 0-2.4 0z" stroke="#111" stroke-width="1" fill="#111"/><path d="M15 7h1V6h-1zM17 7h1V4.5h-1zM19 7h1V3h-1zM21 7h1V1h-1z" fill="#111"/><rect x="28" y="1" width="9" height="6" rx="1" fill="none" stroke="#111"/><rect x="29.5" y="2.5" width="6" height="3" fill="#111"/><rect x="37.5" y="3" width="1" height="2" fill="#111"/></svg></div>
  <div class="topbar"><svg width="8" height="10" viewBox="0 0 8 10"><path d="M6 1L2 5l4 4" stroke="#111" stroke-width="1.4" fill="none"/></svg><span class="title">Steps</span><span class="action small">Upload recipe</span></div>

  <div class="step" style="left:18px;top:73px"><div class="photo" role="img" aria-label="Step 1 photo: egg yolk in a bowl" style="background:linear-gradient(160deg,#e9e6e2,#cdc3b4)"></div><span class="num">01</span><p>Lorem ipsum dolor sit amet, consectetur adipiscing</p></div>
  <div class="step" style="left:129px;top:73px"><div class="photo" role="img" aria-label="Step 2 photo: egg yolks on flour" style="background:linear-gradient(160deg,#ebe7e1,#e3c9a0)"></div><span class="num">02</span><p>Lorem ipsum dolor sit amet, consectetur adipiscing</p></div>
  <div class="step" style="left:18px;top:224px"><div class="photo" role="img" aria-label="Step 3 photo: whisking cream in a bowl" style="background:linear-gradient(160deg,#f6e7b0,#e8e2d4)"></div><span class="num">03</span><p>Lorem ipsum dolor sit amet, consectetur adipiscing</p></div>
  <div class="step" style="left:129px;top:224px"><div class="photo" role="img" aria-label="Step 4 photo: whisking beaten eggs in a pan" style="background:linear-gradient(160deg,#7a5d45,#d9a233)"></div><span class="num">04</span><p>Lorem ipsum dolor sit amet, consectetur adipiscing</p></div>

  <div class="fab"><svg width="12" height="12" viewBox="0 0 12 12"><path d="M6 1v10M1 6h10" stroke="#fff" stroke-width="1.4"/></svg></div>
  <div class="home-bar"></div>
</section>
</body>
</html>
```